Simple elegant business card

General card for a fin and television director.
Just want name, email, phone and address.

Target Market(s)

Prospective employers

Industry/Entity Type

Business

Requirements
Must have
• As above
Nice to have
• Logo but not necessary.
Should not have
• Not too colourful or funky.
• Simplicity and elegance the way to go.

```html
<!DOCTYPE html>
<html lang="en">
<head>
<meta charset="utf-8">
<title>Nora Fields – Business Card</title>
<link rel="stylesheet" href="https://fonts.googleapis.com/css2?family=Source+Sans+3:wght@400&display=swap">
<style>
  :root {
    --backdrop: #2e2119;
    --card-warm: #c85a2c;
    --card-deep: #a8282c;
    --ink: #ffffff;
    --ink-soft: rgba(255, 255, 255, 0.88);
  }
  html, body {
    margin: 0;
    padding: 0;
    width: 1200px;
    height: 1200px;
    overflow: hidden;
    background: var(--backdrop);
    font-family: "Source Sans 3", "Myriad Pro", Arial, sans-serif;
  }
  .business-card {
    position: absolute;
    left: 100px;
    top: 314px;
    width: 1000px;
    height: 572px;
    border-radius: 44px;
    background: linear-gradient(90deg,
      var(--card-warm) 0%,
      var(--card-warm) 16%,
      var(--card-deep) 46%,
      var(--card-deep) 100%);
    color: var(--ink);
  }
  .brand-block {
    position: absolute;
    left: 78px;
    top: 96px;
  }
  .brand-mark {
    display: block;
    width: 150px;
    height: 150px;
    background: var(--ink);
    margin-bottom: 22px;
  }
  .brand-name {
    margin: 0;
    font-size: 60px;
    font-weight: 400;
    line-height: 1;
    letter-spacing: -0.5px;
    white-space: nowrap;
  }
  .contact-block {
    position: absolute;
    left: 500px;
    top: 140px;
    width: 460px;
  }
  .contact-name {
    margin: 0 0 24px;
    font-size: 78px;
    font-weight: 400;
    line-height: 1;
    letter-spacing: 0.5px;
    white-space: nowrap;
  }
  .contact-line {
    margin: 0;
    font-size: 42px;
    line-height: 1.22;
    letter-spacing: 0.5px;
    white-space: nowrap;
  }
  .contact-address {
    margin-top: 14px;
    color: var(--ink-soft);
  }
</style>
</head>
<body>
  <section class="business-card">
    <div class="brand-block">
      <span class="brand-mark" aria-hidden="true"></span>
      <p class="brand-name">Nora Fields</p>
    </div>
    <div class="contact-block">
      <h1 class="contact-name">Nora Fields</h1>
      <p class="contact-line contact-email">norafields@mail.com</p>
      <p class="contact-line contact-phone">+1 310 555 0142</p>
      <p class="contact-line contact-address">1200 Vine Street<br>Los Angeles, CA 90038</p>
    </div>
  </section>
</body>
</html>
```